TalkBridge - Language Coaching Services

Sleek, innovative, trendy design for Language Coaching business.

TalkBridge is a new UK based company that provides Language Coaching services. We offer highly personalized on-line and face to face language courses. We also impart learning techniques workshops based on the latest neuroscience research for second-language acquisition.

Target Market(s)

Industry/Entity Type

Consulting

Contact Information for Business Card

TalkBridge
ElenaVT@talkbridge-demo.co.uk
TalkBridge-demo.co.uk
London, UK

Font styles to use
Sans Serif

```html
<!DOCTYPE html>
<html lang="en">
<head>
<meta charset="UTF-8">
<title>TalkBridge – Business Card</title>
<link href="https://fonts.googleapis.com/css2?family=Montserrat:wght@300;400;600;700&display=swap" rel="stylesheet">
<style>
  :root {
    --bg: #e9ecef;
    --card: #ffffff;
    --blue: #1a8fd0;
    --blue-light: #1ea7e1;
    --blue-dark: #155a8a;
    --navy: #1d4f7a;
    --rule: #2d5f86;
    --tint-1: #f6fafd;
    --tint-2: #e4f0fa;
    --tint-3: #cfe3f4;
    --tint-4: #b9d7ef;
  }
  * { margin: 0; padding: 0; box-sizing: border-box; }
  html, body { width: 1200px; height: 1200px; overflow: hidden; }
  body {
    background: var(--bg);
    font-family: "Montserrat", sans-serif;
    display: flex;
    flex-direction: column;
    align-items: center;
    justify-content: center;
    gap: 50px;
  }
  .card {
    position: relative;
    width: 880px;
    height: 503px;
    background: var(--card);
    overflow: hidden;
    box-shadow: 0 6px 22px rgba(0,0,0,.18);
  }

  /* Front */
  .brand {
    position: absolute;
    left: 60px;
    top: 112px;
    width: 310px;
    display: flex;
    flex-direction: column;
    align-items: center;
    gap: 24px;
  }
  .brand-mark {
    width: 118px;
    height: 118px;
    border: 9px solid var(--blue);
    border-radius: 50%;
  }
  .brand-name {
    font-weight: 600;
    font-size: 40px;
    letter-spacing: 1px;
    color: var(--blue);
    text-transform: uppercase;
    white-space: nowrap;
  }
  .divider {
    position: absolute;
    left: 400px;
    top: 70px;
    width: 2px;
    height: 200px;
    background: var(--rule);
  }
  .person {
    position: absolute;
    left: 440px;
    top: 82px;
  }
  .person-name {
    font-weight: 700;
    font-size: 30px;
    color: var(--blue);
    text-transform: uppercase;
    line-height: 1;
  }
  .person-title {
    font-weight: 300;
    font-size: 20px;
    color: var(--navy);
    text-transform: uppercase;
    margin-top: 6px;
  }
  .contact {
    list-style: none;
    margin-top: 34px;
    display: flex;
    flex-direction: column;
    gap: 10px;
  }
  .contact li {
    display: flex;
    align-items: center;
    gap: 12px;
    font-weight: 400;
    font-size: 19px;
    color: var(--navy);
    white-space: nowrap;
  }
  .contact svg { width: 20px; height: 20px; flex: none; }

  .band {
    position: absolute;
    left: 0;
    top: 360px;
    width: 100%;
    height: 62px;
    background: linear-gradient(90deg, var(--blue-light), var(--blue) 55%, var(--blue-dark));
    display: flex;
    align-items: center;
    padding-left: 70px;
    gap: 16px;
    color: #fff;
    font-weight: 300;
    font-size: 24px;
  }
  .band svg { width: 24px; height: 28px; }
  .band-mark {
    position: absolute;
    right: 110px;
    top: -16px;
    width: 94px;
    height: 94px;
    border-radius: 50%;
    background: #fff;
    border: 7px solid var(--blue);
  }

  /* Back */
  .pattern-field {
    position: absolute;
    inset: 0;
    background:
      radial-gradient(circle at 12% 20%, var(--tint-3) 0, transparent 32%),
      radial-gradient(circle at 38% 78%, var(--tint-3) 0, transparent 30%),
      radial-gradient(circle at 66% 30%, var(--tint-2) 0, transparent 34%),
      radial-gradient(circle at 88% 82%, var(--tint-3) 0, transparent 30%),
      radial-gradient(ellipse at 50% 50%, var(--tint-1) 0, transparent 70%),
      linear-gradient(135deg, var(--tint-2), var(--tint-1) 35%, var(--tint-2) 60%, var(--tint-1));
  }
  .pattern-field::after {
    content: "";
    position: absolute;
    inset: 0;
    background: linear-gradient(180deg, rgba(185,215,239,.25), rgba(255,255,255,0) 45%, rgba(185,215,239,.3));
  }
  .back-mark {
    position: absolute;
    right: 52px;
    top: 160px;
    width: 74px;
    height: 74px;
    border-radius: 50%;
    background: #fff;
    border: 6px solid var(--blue-dark);
    box-shadow: 0 0 0 10px rgba(255,255,255,.6);
  }
</style>
</head>
<body>

  <section class="card card-front">
    <div class="brand">
      <div class="brand-mark"></div>
      <div class="brand-name">TalkBridge</div>
    </div>

    <div class="divider"></div>

    <div class="person">
      <div class="person-name">Your Name</div>
      <div class="person-title">Your Title</div>
      <ul class="contact">
        <li>
          <svg viewBox="0 0 20 20" aria-hidden="true"><circle cx="10" cy="10" r="10" fill="#1a8fd0"/><rect x="4.5" y="6.5" width="11" height="7" rx="1" fill="#fff"/><path d="M4.8 7 10 11 15.2 7" stroke="#1a8fd0" stroke-width="1.2" fill="none"/></svg>
          ElenaVT@talkbridge-demo.co.uk
        </li>
        <li>
          <svg viewBox="0 0 20 20" aria-hidden="true"><circle cx="10" cy="10" r="9" fill="none" stroke="#1a8fd0" stroke-width="2"/><circle cx="10" cy="10" r="5" fill="none" stroke="#1a8fd0" stroke-width="1.5"/><path d="M5 10h10M10 5v10" stroke="#1a8fd0" stroke-width="1.2"/></svg>
          TalkBridge-demo.co.uk
        </li>
      </ul>
    </div>

    <div class="band">
      <svg viewBox="0 0 24 28" aria-hidden="true"><path d="M12 1C6 1 2 5.5 2 11c0 7 10 16 10 16s10-9 10-16C22 5.5 18 1 12 1z" fill="#fff"/><circle cx="12" cy="11" r="4" fill="#1ea7e1"/></svg>
      London, UK
      <div class="band-mark"></div>
    </div>
  </section>

  <section class="card card-back">
    <div class="pattern-field" role="img" aria-label="Pale blue repeating brand emblem pattern covering the whole card back"></div>
    <div class="back-mark"></div>
  </section>

</body>
</html>
```